Lumen Kinetics Web Design Project

We need to update our web design for our company. Lumen Kinetics™ is a series of Development (Training) Programs that we deliver both for the General Public as well as Corporate Business.

Much of the content needs a refresh but we are keen to get some thoughts now on design and layout, predominantly front page. Happy to take any comments on the content if you think that is relevant as well.

We might look to move the current video clip and bring a more generic 'inspirational' clip to the front page. A good example of this is www.mindcraftoz.example.au

Our courses have a very similar market to Gerald Whitcombe type courses ... both General Public and Corporate business.

Refer our website www.lumenkinetics.example.com

Target Market(s)

General Public as well as Corporate Business. Courses are designed for all. Gerald Whitcombe would be a good 'feel' for what we do.

Industry/Entity Type

Business

Requirements
Must have
• Must have a 'leading edge' type feel to it.
Must look professional.

```html
<!DOCTYPE html>
<html lang="en">
<head>
<meta charset="utf-8">
<title>Lumen Kinetics</title>
<link rel="stylesheet" href="https://fonts.googleapis.com/css2?family=Open+Sans:wght@400;600;700&family=Roboto+Condensed:wght@300;400&family=Oswald:wght@400;500&family=Lora:ital@1&display=swap">
<style>
:root{
  --blue:#0a4fa6;
  --blue-dark:#053f8c;
  --blue-deep:#043476;
  --sky:#2a7ed6;
  --orange:#c9531a;
  --gold:#f3a91b;
  --ink:#333;
  --grey:#666;
  --band:#e9eaec;
  --line:#d6d6d6;
  --black:#1e1e1e;
}
*{box-sizing:border-box;margin:0;padding:0}
html,body{width:755px;height:1200px;overflow:hidden;background:#fff}
body{position:relative;font-family:'Open Sans',Arial,sans-serif;color:var(--ink)}
.wrap{position:absolute;left:88px;width:579px}

/* header */
.site-header{position:absolute;top:0;left:0;width:755px;height:86px;background:#fff}
.brand{position:absolute;left:88px;top:22px;display:flex;align-items:center;gap:10px}
.brand-dot{width:14px;height:14px;border-radius:50%;background:var(--sky)}
.brand-name{font-family:'Open Sans',sans-serif;font-size:24px;font-weight:600;color:var(--blue);line-height:1}
.social{position:absolute;left:526px;top:8px;display:flex;flex-direction:column;gap:7px}
.social span{width:10px;height:10px;border-radius:2px;background:#bdbdbd;display:block}
.call{position:absolute;left:551px;top:9px;border-left:2px solid #999;padding-left:5px}
.call small{display:block;font-family:'Oswald',sans-serif;font-size:12px;color:#555;letter-spacing:.5px;line-height:1}
.call strong{display:block;font-family:'Oswald',sans-serif;font-weight:500;font-size:21px;color:#444;line-height:1.1}
.tagline{position:absolute;right:88px;top:60px;font-family:'Roboto Condensed',sans-serif;font-size:12.5px;color:var(--orange);white-space:nowrap}

/* nav */
.main-nav{position:absolute;top:86px;left:0;width:755px;height:30px;background:var(--blue);border-bottom:1px solid #2d6cc0}
.main-nav ul{list-style:none;display:flex;gap:19px;position:absolute;left:99px;top:8px}
.main-nav li{font-size:9.5px;font-weight:600;color:#fff;white-space:nowrap}

/* hero */
.hero{position:absolute;top:116px;left:0;width:755px;height:272px;background:radial-gradient(ellipse at 30% 40%,#1667c9,#0a4fa6 70%)}
.video-frame{position:absolute;left:88px;top:29px;width:325px;height:206px;background:#fff;padding:5px}
.video{width:100%;height:100%;background:radial-gradient(ellipse at 50% 45%,#3d86e6,#0b3f9a 75%,#061f52)}
.hero-copy{position:absolute;left:438px;top:22px;width:240px}
.hero-copy h1{font-family:'Roboto Condensed',sans-serif;font-weight:400;font-size:23px;line-height:29px;color:#fff}
.hero-copy hr{border:0;border-top:1px solid #3d7dcc;margin:12px 0 20px;width:200px}
.btn-learn{display:inline-block;background:var(--gold);color:#fff;font-size:11px;font-weight:700;padding:7px 10px;border-radius:14px;border:2px solid #e0930b;box-shadow:0 1px 2px rgba(0,0,0,.3)}

/* programs band */
.programs{position:absolute;top:388px;left:0;width:755px;height:178px;background:var(--band)}
.program{position:absolute;top:30px;width:131px;text-align:center}
.program .photo{height:101px;box-shadow:0 3px 5px rgba(0,0,0,.35)}
.program p{margin-top:12px;font-size:12px;color:#111}

/* content */
.welcome{position:absolute;left:88px;top:590px;width:372px}
.welcome h2{font-family:'Roboto Condensed',sans-serif;font-weight:400;font-size:24px;color:var(--blue)}
.welcome .lead{font-size:8px;line-height:13px;color:var(--grey);margin-top:6px}
.contact-bar{margin-top:13px;background:var(--black);color:#fff;padding:3px 8px 5px}
.contact-bar b{display:block;font-family:'Open Sans',sans-serif;font-weight:400;font-size:15px;line-height:18px}
.contact-bar small{font-size:8px;color:#ccc}
.benefits{list-style:none;margin-top:14px}
.benefits li{font-size:8.5px;color:var(--grey);margin-bottom:11px;padding-left:20px;position:relative}
.benefits li::before{content:'›';position:absolute;left:5px;top:-4px;font-size:13px;font-weight:700;color:var(--orange)}
.experience h3{font-family:'Roboto Condensed',sans-serif;font-weight:400;font-size:17px;color:#222;margin-top:18px}
.steps{list-style:none;margin-top:10px}
.steps li{display:flex;align-items:center;height:36px;font-family:'Roboto Condensed',sans-serif;font-size:12px;color:#555}
.steps .num{width:30px;height:30px;border-radius:50%;background:#e4e4e4;border:2px dotted #ccc;display:flex;align-items:center;justify-content:center;font-size:16px;color:#333;margin-right:14px}
.steps em{font-style:normal;color:var(--orange);margin-left:3px}

.sidebar{position:absolute;left:490px;width:177px}
.testimonial{top:596px;height:120px;background:#f1f1f1;border:1px solid #e0e0e0;padding:10px 12px}
.testimonial h4{font-family:'Roboto Condensed',sans-serif;font-weight:400;font-size:17px;color:#222;padding-left:38px}
.testimonial p{font-family:'Lora',serif;font-style:italic;font-size:7.6px;line-height:13.5px;color:#999;margin-top:6px}
.testimonial .quote{position:absolute;font-family:Georgia,serif;font-size:50px;color:#ddd;line-height:1}
.client{position:absolute;left:522px;top:736px;font-size:8px;font-weight:700;color:var(--blue)}
.newsletter{top:766px;height:72px;background:var(--black);padding:8px 12px}
.newsletter h4{font-family:'Roboto Condensed',sans-serif;font-weight:300;font-size:17px;color:#fff;display:flex;align-items:center;gap:6px}
.signup{display:flex;margin-top:9px}
.signup span{flex:1;height:20px;background:#fff}
.signup b{background:var(--blue);color:#fff;font-family:'Oswald',sans-serif;font-weight:400;font-size:11px;padding:3px 5px;border:1px solid #4a86d4}
.news{top:868px;height:188px;border:1px solid var(--line);padding:10px 10px}
.news h4{font-family:'Roboto Condensed',sans-serif;font-weight:400;font-size:17px;color:#222}
.news article{padding:8px 0 10px;border-bottom:1px solid #eee}
.news time{font-size:8px;color:var(--blue)}
.news p{font-size:8px;line-height:13px;color:var(--grey)}

/* footer */
.site-footer{position:absolute;top:1084px;left:0;width:755px;height:86px;background:var(--blue-dark)}
.fcol{position:absolute;top:18px}
.fcol h5{font-family:'Roboto Condensed',sans-serif;font-weight:400;font-size:15px;color:#fff;display:flex;align-items:center;gap:7px;border-bottom:1px solid #3a71bb;padding-bottom:2px;margin-bottom:8px;width:110px}
.fcol p{font-size:8.5px;font-weight:600;color:#fff;line-height:14px}
.footer-nav{position:absolute;top:1170px;left:0;width:755px;height:30px;background:var(--blue-deep)}
.footer-nav ul{list-style:none;display:flex;gap:27px;position:absolute;left:107px;top:3px}
.footer-nav li{font-size:8px;color:#fff;white-space:nowrap}
.footer-nav small{position:absolute;top:17px;width:100%;text-align:center;font-size:7px;color:#fff}
</style>
</head>
<body>

<header class="site-header">
  <div class="brand"><span class="brand-dot"></span><span class="brand-name">Lumen Kinetics™</span></div>
  <div class="social"><span></span><span></span><span></span></div>
  <div class="call"><small>CALL US ON</small><strong>61(0) 400 555 019</strong></div>
  <div class="tagline">A NEW WAY OF THINKNG TO CREAT, A NEW WAY OF BEING</div>
</header>

<nav class="main-nav">
  <ul><li>Home</li><li>Lumen Kinetics™</li><li>About Us</li><li>Our Programs</li><li>Events</li><li>Our Products</li><li>Articles &amp; Resources</li><li>Contact Us</li></ul>
</nav>

<section class="hero">
  <div class="video-frame"><div class="video" role="img" aria-label="Introductory video player with a blue title screen"></div></div>
  <div class="hero-copy">
    <h1>IF THERE IS ONE THING YOU DO THIS YEAR..... MAKE SURE IT'S LUMEN KINETICS™</h1>
    <hr>
    <span class="btn-learn">LEARN MORE</span>
  </div>
</section>

<section class="programs">
  <div class="program" style="left:88px"><div class="photo" role="img" aria-label="Group seated in a circle at a community session" style="background:linear-gradient(#8a8275,#4d4a45)"></div><p>Community Training</p></div>
  <div class="program" style="left:237px"><div class="photo" role="img" aria-label="Children in sports kit with a ball on grass" style="background:linear-gradient(#6f8a4a,#3e5a24)"></div><p>Children Training</p></div>
  <div class="program" style="left:386px"><div class="photo" role="img" aria-label="Dogs and handlers at an outdoor training class" style="background:linear-gradient(#5b6878,#3c4a3a)"></div><p>Animals Training</p></div>
  <div class="program" style="left:535px"><div class="photo" role="img" aria-label="Business team seated around a meeting table" style="background:linear-gradient(#a7b0b8,#5a6470)"></div><p>Busimessman Training</p></div>
</section>

<main>
  <section class="welcome">
    <h2>WELCOME TO LUMEN KINETICS</h2>
    <p class="lead">Lumen Kinetics™ is a leading edge model which introduces a new lens to view yourself and the world you operate within. Lumen Kinetics™ is for everyone. It's all about Transformation and Skills for Life.</p>
    <div class="contact-bar"><b>Contact Us Now</b><small>you will never look back!</small></div>
    <ul class="benefits">
      <li>Improve your health and wellbeing</li>
      <li>Create a new fun and healthy culture</li>
      <li>Learn new ways to manage stress and create balance in your life</li>
      <li>Enhance your communication skills and strengthen your relationships</li>
      <li>Learn new ways to Transform and create all that you have ever wanted.</li>
    </ul>
    <div class="experience">
      <h3>EXPERIENCE FOR YOURSELF</h3>
      <ol class="steps">
        <li><span class="num">1</span>LUMEN KINETICS™ <em>FOR YOU</em></li>
        <li><span class="num">2</span>LUMEN KINETICS™ <em>FOR CHILDREN AND SCHOOLS</em></li>
        <li><span class="num">3</span>LUMEN KINETICS™ <em>FOR BUSINESS</em></li>
        <li><span class="num">4</span>LUMEN KINETICS™ <em>FOR ANIMALS</em></li>
        <li><span class="num">5</span>LUMEN KINETICS™ <em>FOR COMMUNITY</em></li>
      </ol>
    </div>
  </section>

  <aside>
    <div class="sidebar testimonial">
      <span class="quote" style="left:4px;top:-2px">“</span>
      <span class="quote" style="right:6px;bottom:-22px">”</span>
      <h4>TESTIMONIAL</h4>
      <p>Lorem Ipsum is simply dummy text of the printing and typesetting industry. Lorem Ipsum has been the industry's standard dummy text ever since the 1500s, printer took a galley of type.</p>
    </div>
    <div class="client">- Client's Name</div>
    <div class="sidebar newsletter">
      <h4><svg width="16" height="12" viewBox="0 0 16 12"><rect x="0.5" y="0.5" width="15" height="11" fill="#fff"/><path d="M1 1l7 6 7-6" fill="none" stroke="#1e1e1e" stroke-width="1.2"/></svg>NEWSLETTER</h4>
      <div class="signup"><span></span><b>SUBSCRIBE</b></div>
    </div>
    <div class="sidebar news">
      <h4>LATEST NEWS</h4>
      <article><time>31 JUNE 2013</time><p>It is a long established fact that a reader will be distracted by the readable content of a page when looking at</p></article>
      <article style="border:0"><time>31 JUNE 2013</time><p>It is a long established fact that a reader will be distracted by the readable content of a page when looking at</p></article>
    </div>
  </aside>
</main>

<footer class="site-footer">
  <div class="fcol" style="left:88px">
    <h5><svg width="9" height="12" viewBox="0 0 9 12"><path d="M4.5 0a4.5 4.5 0 0 0-4.5 4.5C0 8 4.5 12 4.5 12S9 8 9 4.5A4.5 4.5 0 0 0 4.5 0z" fill="#fff"/><circle cx="4.5" cy="4.5" r="1.7" fill="#053f8c"/></svg>ADDRESS</h5>
    <p>PO BOX 17, HARBOUR LANE EAST<br>VIC 8000 AUSTRALIA</p>
  </div>
  <div class="fcol" style="left:320px">
    <h5><svg width="9" height="12" viewBox="0 0 9 12"><path d="M2 0h2l1 3-1.5 1a6 6 0 0 0 2 4L7 7l2 1.5V11a1 1 0 0 1-1 1C3 11 0 6 0 2a2 2 0 0 1 2-2z" fill="#fff"/></svg>PHONE NO</h5>
    <p>+61 (3) 9000 0147<br>+61 (0) 400 555 019</p>
  </div>
  <div class="fcol" style="left:554px">
    <h5><svg width="12" height="9" viewBox="0 0 12 9"><rect width="12" height="9" fill="#fff"/><path d="M0 0l6 5 6-5" fill="none" stroke="#053f8c"/></svg>EMAIL</h5>
    <p style="font-weight:400;font-size:7.5px">info@lumenkinetics.example.com</p>
  </div>
</footer>
<div class="footer-nav">
  <ul><li>Home</li><li>Lumen Kinetics™</li><li>About Us</li><li>Our Programs</li><li>Events</li><li>Our Products</li><li>Articles &amp; Resources</li><li>Contact Us</li></ul>
  <small>Copyright © 2013 Lumen Kinetics. All Rights Reserved.</small>
</div>

</body>
</html>
```